Desk Allies Business Card

Contact Information for Business Card

Janne Voutilainen
Managing Director

3/47 Brindle Street Mitchell ACT 2911

Tel: +61 02 6257 3140
Mob: +61 0427 315 846

Email: janne@deskallies.com.au
Web: www.deskallies.com.au

Colors

Designer to choose colors to be used in the design.

Requirements
Must have
• Logo, Name, Title, Address, Telephone, Mobile, Email Address and Website
• "Desk Ally International Pty Ltd"

```html
<!DOCTYPE html>
<html lang="en">
<head>
<meta charset="utf-8">
<title>Desk Allies Business Card</title>
<link rel="stylesheet" href="https://fonts.googleapis.com/css2?family=Bebas+Neue&display=swap">
<style>
  :root {
    --page: #ececec;
    --card: #ffffff;
    --brand-blue: #1f73b8;
    --text-grey: #8a8a8a;
  }
  * { margin: 0; padding: 0; box-sizing: border-box; }
  html, body {
    width: 1200px;
    height: 1200px;
    overflow: hidden;
    background: var(--page);
    font-family: "Bebas Neue", "Arial Narrow", sans-serif;
  }
  .canvas { position: relative; width: 1200px; height: 1200px; }

  .card-back {
    position: absolute;
    left: 235px; top: 88px;
    width: 730px; height: 419px;
    background: var(--brand-blue);
  }

  .card-front {
    position: absolute;
    left: 147px; top: 598px;
    width: 906px; height: 519px;
    background: var(--card);
    overflow: hidden;
  }
  .pattern-field {
    position: absolute;
    left: 0; top: 0;
    width: 906px; height: 519px;
  }

  .brand {
    position: absolute;
    left: 63px; top: 54px;
    display: flex;
    align-items: center;
    gap: 12px;
  }
  .brand-dot {
    width: 62px; height: 62px;
    border-radius: 50%;
    background: var(--brand-blue);
    flex: none;
  }
  .brand-text { display: flex; flex-direction: column; }
  .brand-name {
    font-size: 42px;
    line-height: 40px;
    letter-spacing: 1.5px;
    color: var(--brand-blue);
  }
  .brand-entity {
    margin-top: 2px;
    font-size: 16px;
    line-height: 16px;
    letter-spacing: 3.6px;
    color: var(--text-grey);
    white-space: nowrap;
  }

  .person { position: absolute; left: 63px; top: 193px; }
  .person-name {
    font-size: 40px;
    line-height: 1;
    letter-spacing: 0.5px;
    color: var(--brand-blue);
    font-weight: 400;
  }
  .person-title {
    margin-top: 6px;
    font-size: 20px;
    letter-spacing: 1.8px;
    color: var(--text-grey);
  }

  .contact {
    position: absolute;
    left: 63px; top: 325px;
    list-style: none;
  }
  .contact li {
    font-size: 20px;
    line-height: 30.5px;
    letter-spacing: 1.8px;
    color: var(--text-grey);
    white-space: nowrap;
  }
</style>
</head>
<body>
<main class="canvas">
  <section class="card-back" role="img" aria-label="Card back: all-over blue and white interlocking loop pattern"></section>

  <section class="card-front">
    <svg class="pattern-field" viewBox="0 0 906 519" role="img" aria-label="Diamond-shaped field of blue interlocking loop pattern">
      <polygon points="521,257 800,-22 1080,257 800,536" fill="var(--brand-blue)" opacity="0.85"/>
    </svg>

    <div class="brand">
      <span class="brand-dot"></span>
      <div class="brand-text">
        <span class="brand-name">Desk Allies</span>
        <span class="brand-entity">Desk Ally International Pty Ltd</span>
      </div>
    </div>

    <div class="person">
      <h1 class="person-name">Janne Voutilainen</h1>
      <p class="person-title">Managing Director</p>
    </div>

    <ul class="contact">
      <li>3/47 Brindle Street Mitchell ACT 2911</li>
      <li>Tel: +61 02 6257 3140</li>
      <li>Mob: +61 0427 315 846</li>
      <li>Email: janne@deskallies.com.au</li>
      <li>Web: www.deskallies.com.au</li>
    </ul>
  </section>
</main>
</body>
</html>
```